Web site for small printshop

I am looking for a website for small printshop in Iceland, mainly serving university students and artist.

We print posters, flyers, business cards and more.

In addition to our current website, I would like to include design tool, (fx. www.quarvelink.com, www.tandorizo.com or something similar) jobs upload, shopping chart.
Updates

Great work, I am really amazed of the quality of work i am seeing here.

Really way beyond my expectation

GOOD JOB - all of you ! 

Hi all.

The designs submitted have been great, way better than expected.
I really did not expect this level of quality.

Some have been asking me for feedback on their designs, and I will try 
to send some feedback here, without spoiling your creativity.

Likes:
- when the colors of my logo is used in menus, buttons etc.
- simple, not to crowded look.

Dislikes.
- Dark and heavy design
- Lot of text and buttons (crowded look)

Extra info.
- top line (before menus) will contain: Tel - email - language
- menu line will have 5 categories: Home - service - submission of works - FAQ - about us
- 3 large buttons:  Job submit - Job design - ask for offer

LOVE YOUR WORK - great designs so far :)

Target Market(s)

University Students, Artists. Age group 20-30

Industry/Entity Type

University

Requirements
Must have
• The website must be easy to use, clean looking.

```html
<!DOCTYPE html>
<html lang="en">
<head>
<meta charset="utf-8">
<title>Korvaprent</title>
<link rel="stylesheet" href="https://fonts.googleapis.com/css2?family=Source+Sans+3:wght@400;600&family=Arimo:wght@400&display=swap">
<style>
:root{
  --red:#d13f38;
  --red-dark:#c2332c;
  --yellow:#f5d32a;
  --black:#000;
  --ink:#222;
  --grey-bg:#f5f5f5;
  --line:#dcdcdc;
  --footer:#111;
}
*{margin:0;padding:0;box-sizing:border-box}
html,body{width:1051px;height:1200px;overflow:hidden;background:#fff}
body{position:relative;font-family:"Arimo",Arial,sans-serif;color:var(--ink)}
.abs{position:absolute}
.heading-font{font-family:"Source Sans 3",Arial,sans-serif}

.topbar{left:0;top:0;width:1051px;height:25px;background:#ececec;border-bottom:1px solid #ddd}
.topbar-links{right:106px;top:6px;font-size:11px;letter-spacing:.3px;color:#333;white-space:nowrap}
.topbar-links span{margin-left:14px}

.header{left:0;top:25px;width:1051px;height:70px;background:linear-gradient(#fff,#f4f4f4);border-bottom:1px solid #e2e2e2}
.brand{left:105px;top:12px;display:flex;align-items:center;gap:10px}
.brand-square{width:36px;height:36px;background:var(--red)}
.brand-name{font-family:"Source Sans 3",Arial,sans-serif;font-weight:600;font-size:30px;color:#333;letter-spacing:.5px}
.nav{top:26px;font-family:"Source Sans 3",Arial,sans-serif;font-size:17px;color:#222}
.nav.active{color:var(--red)}

.hero{left:0;top:95px;width:1051px;height:376px;background:var(--red)}
.hero-title{left:108px;top:102px;font-family:"Source Sans 3",Arial,sans-serif;font-size:41px;line-height:47px;color:#fff}
.hero-title em{font-style:normal;color:var(--yellow)}
.hero-art{left:534px;top:45px;width:425px;height:290px;border-radius:45% 55% 50% 40%;background:radial-gradient(ellipse at 55% 45%,#e0625b 0%,#d7524b 45%,rgba(209,63,56,0) 75%)}

.steps{left:0;top:471px;width:1051px;height:62px;background:var(--black)}
.step-label{top:16px;font-family:"Source Sans 3",Arial,sans-serif;font-size:26px;color:#fff}
.steps svg{position:absolute}

.welcome-title{left:104px;top:558px;font-family:"Source Sans 3",Arial,sans-serif;font-size:28px;color:var(--red)}
.welcome-text{left:105px;top:606px;width:535px;font-size:11px;line-height:17.5px;letter-spacing:.3px;color:#222}
.welcome-text p{margin-bottom:17.5px}

.quote{left:667px;top:558px;width:248px;height:318px;background:#f3f3f3;border:1px solid #d8d8d8}
.quote-head{left:0;top:0;width:246px;height:35px;background:linear-gradient(#e8453d,var(--red-dark));color:#fff;font-family:"Source Sans 3",Arial,sans-serif;font-size:18px;padding:7px 0 0 15px}
.field{left:12px;width:222px;height:30px;background:#fff;border:1px solid #cfcfcf;font-family:"Source Sans 3",Arial,sans-serif;font-size:13px;color:#666;padding:6px 10px}
.submit{left:155px;top:274px;width:77px;height:30px;background:linear-gradient(#e8453d,var(--red-dark));color:#fff;font-family:"Source Sans 3",Arial,sans-serif;font-size:13px;text-align:center;line-height:30px}

.lower{left:0;top:908px;width:1051px;height:213px;background:var(--grey-bg);border-top:1px solid var(--line)}
.divider{left:668px;top:0;width:1px;height:205px;background:var(--line)}
.section-title{top:15px;font-family:"Source Sans 3",Arial,sans-serif;font-size:28px;color:var(--red)}
.service-list{list-style:none;top:60px;font-size:11px;letter-spacing:.3px;color:#222}
.service-list li{height:26.3px;padding-left:16px;position:relative}
.service-list li::before{content:"";position:absolute;left:2px;top:2px;width:5px;height:5px;border-right:1.5px solid var(--red);border-top:1.5px solid var(--red);transform:rotate(45deg)}
.portfolio-box{left:689px;top:60px;width:228px;height:117px;background:#b3b3b3;color:#fff;font-family:"Source Sans 3",Arial,sans-serif;font-size:16px;display:flex;align-items:center;justify-content:center}

.footer{left:0;top:1121px;width:1051px;height:79px;background:var(--footer);border-top:4px solid var(--red)}
.footer-links{left:105px;top:23px;font-size:9.5px;color:#ccc;letter-spacing:.3px}
.footer-copy{left:105px;top:41px;font-size:10px;color:#ccc;letter-spacing:.3px}
.follow{left:805px;top:32px;font-size:9.5px;color:#ccc}
.social{top:22px;width:28px;height:28px;border-radius:50%;background:#bdbdbd}
</style>
</head>
<body>

<div class="abs topbar">
  <div class="abs topbar-links">Login | Register | Cart<span>Call Us: 555 010 2030</span><span>Email:info@korvaprent.is</span></div>
</div>

<header class="abs header">
  <div class="abs brand"><div class="brand-square"></div><div class="brand-name">KORVAPRENT</div></div>
  <div class="abs nav active" style="left:467px">HOME</div>
  <div class="abs nav" style="left:539px">ABOUT US</div>
  <div class="abs nav" style="left:640px">SERVICES</div>
  <div class="abs nav" style="left:732px">UPLOAD &amp; PRINT</div>
  <div class="abs nav" style="left:878px">CONTACT</div>
</header>

<section class="abs hero">
  <h1 class="abs hero-title" style="font-weight:400">We Print Posters,<br>Flyers, Business Cards<br>&amp; <em>More...</em></h1>
  <div class="abs hero-art" role="img" aria-label="Dotted map of Iceland with a printed document illustration"></div>
</section>

<section class="abs steps">
  <svg style="left:121px;top:11px" width="42" height="40" viewBox="0 0 42 40"><rect x="2" y="2" width="38" height="27" rx="3" fill="none" stroke="#f5d32a" stroke-width="4"/><rect x="17" y="29" width="8" height="6" fill="#f5d32a"/><rect x="10" y="34" width="22" height="4" rx="2" fill="#f5d32a"/></svg>
  <div class="abs step-label" style="left:181px">SIGN UP</div>
  <svg style="left:295px;top:15px" width="30" height="34" viewBox="0 0 30 34"><path d="M2 2l13 15L2 32M14 2l13 15-13 15" fill="none" stroke="#555" stroke-width="3"/></svg>

  <svg style="left:348px;top:10px" width="42" height="42" viewBox="0 0 42 42"><path d="M38 3c2 2-9 16-13 20l-5-5C24 14 36 1 38 3z" fill="#f5d32a"/><path d="M17 20l5 5c-2 6-8 14-20 14 5-4 3-11 8-16 2-2 5-3 7-3z" fill="#f5d32a"/></svg>
  <div class="abs step-label" style="left:399px">DESIGN</div>
  <svg style="left:498px;top:15px" width="30" height="34" viewBox="0 0 30 34"><path d="M2 2l13 15L2 32M14 2l13 15-13 15" fill="none" stroke="#555" stroke-width="3"/></svg>

  <svg style="left:546px;top:9px" width="44" height="44" viewBox="0 0 44 44"><circle cx="22" cy="22" r="19" fill="none" stroke="#f5d32a" stroke-width="4"/><text x="22" y="31" text-anchor="middle" font-family="Arial,sans-serif" font-weight="700" font-size="26" fill="#f5d32a">$</text></svg>
  <div class="abs step-label" style="left:600px">PAYMENT</div>
  <svg style="left:734px;top:15px" width="30" height="34" viewBox="0 0 30 34"><path d="M2 2l13 15L2 32M14 2l13 15-13 15" fill="none" stroke="#555" stroke-width="3"/></svg>

  <svg style="left:790px;top:10px" width="34" height="42" viewBox="0 0 34 42"><path d="M0 0h22l12 12v30H0z" fill="#f5d32a"/><path d="M22 0v12h12z" fill="#000"/></svg>
  <div class="abs step-label" style="left:836px">PRINT</div>
</section>

<h2 class="abs welcome-title" style="font-weight:400">Welcome to our site</h2>
<div class="abs welcome-text">
  <p>&nbsp;Lorem ipsum dolor sit amet, consectetur adipiscing elit. Quisque commodo tortor non purus porttitor sagittis. Sed nec ipsum sit amet tortor rutrum commodo imperdiet vitae justo. Sed ornare sem et quam porta vulputate. Sed a eros et odio adipiscing elementum vel a diam. Donec ut neque eget lacus placerat pharetra a nec dolor. Sed imperdiet risus sit amet feugiat laoreet. Cras ut leo aliquet, blandit sapien vel, interdum nisl.</p>
  <p>Etiam tempus congue ultrices. Sed odio nisi, scelerisque vel consectetur sit amet, tempus quis libero. Proin rhoncus aliquam est dignissim laoreet. Mauris id pharetra massa. Aliquam venenatis dapibus turpis viverra iaculis.</p>
  <p>Nunc cursus vel leo vitae blandit. Aliquam ultrices in massa ac convallis. Sed consectetur tempor velit non ullamcorper. Sed malesuada metus sed semper rhoncus. Morbi lobortis placerat libero quis vestibulum. In aliquet ornare convallis. Nulla vitae lectus augue. Mauris a gravida sem. Morbi lobortis placerat libero quis vestibulum. In aliquet ornare convallis. Nulla vitae lectus augue. Mauris a gravida sem.</p>
</div>

<aside class="abs quote">
  <div class="abs quote-head">Request a Qoute</div>
  <div class="abs field" style="top:48px">Name</div>
  <div class="abs field" style="top:94px">Email</div>
  <div class="abs field" style="top:140px">Phone</div>
  <div class="abs field" style="top:186px;height:74px;padding:8px 14px">Your Quiry</div>
  <div class="abs submit">SUBMIT</div>
</aside>

<section class="abs lower">
  <div class="abs divider"></div>
  <h2 class="abs section-title" style="left:103px;font-weight:400">Services</h2>
  <ul class="abs service-list" style="left:107px"><li>Lorem ipsum dolor</li><li>Adipiscing elit quisque</li><li>Sed odio nisi, scelerisque</li><li>Sed consectetur tempor</li><li>Nunc cursus vel leo vitae</li></ul>
  <ul class="abs service-list" style="left:290px"><li>Lorem ipsum dolor</li><li>Adipiscing elit quisque</li><li>Sed odio nisi, scelerisque</li><li>Sed consectetur tempor</li><li>Nunc cursus vel leo vitae</li></ul>
  <ul class="abs service-list" style="left:484px"><li>Lorem ipsum dolor</li><li>Adipiscing elit quisque</li><li>Sed odio nisi, scelerisque</li><li>Sed consectetur tempor</li><li>Nunc cursus vel leo vitae</li></ul>

  <h2 class="abs section-title" style="left:688px;font-weight:400">Portfolio</h2>
  <svg class="abs" style="left:673px;top:112px" width="8" height="12" viewBox="0 0 8 12"><path d="M8 0v12L0 6z" fill="#d13f38"/></svg>
  <div class="abs portfolio-box">Your work will goes here</div>
  <svg class="abs" style="left:926px;top:112px" width="8" height="12" viewBox="0 0 8 12"><path d="M0 0v12l8-6z" fill="#d13f38"/></svg>
</section>

<footer class="abs footer">
  <div class="abs footer-links">Home &nbsp;| &nbsp;About Us | &nbsp;Services &nbsp;| &nbsp;Upload &amp; Print &nbsp;| &nbsp;Contact</div>
  <div class="abs footer-copy">©Copyright 2013 Korvaprent. All Rights Reserved</div>
  <div class="abs follow">Folow Us On:</div>
  <div class="abs social" style="left:876px"></div>
  <div class="abs social" style="left:915px"></div>
</footer>

</body>
</html>
```